stationary design
Brightway Journeys
Project: stationary design
stationary design - Travel
Creative Brief
Professional
Ibrahim Naseer
Managing Director
H. Fehimaage, Kanbaafaru Higun, Male' Maldives.
naseer@brightwayjourney.example
www.brightwayjourney.example

```html
<!DOCTYPE html>
<html lang="en">
<head>
<meta charset="utf-8">
<title>Brightway Journeys — Business Card</title>
<link href="https://fonts.googleapis.com/css2?family=Marcellus&family=Cormorant+Garamond:wght@500;600&display=swap" rel="stylesheet">
<style>
  :root {
    --navy: #123a78;
    --orange: #f2a21c;
    --paper: #ffffff;
    --stage: #e6e7e9;
    --muted: #4a5b78;
  }
  * { box-sizing: border-box; margin: 0; padding: 0; }
  html, body {
    width: 1200px; height: 984px; overflow: hidden;
    background: var(--stage);
  }
  .sheet {
    position: relative; width: 1200px; height: 984px;
    display: flex; flex-direction: column; align-items: center; justify-content: center; gap: 60px;
  }
  .card {
    position: relative; width: 700px; height: 400px;
    border-radius: 26px; overflow: hidden;
    box-shadow: 0 6px 18px rgba(0,0,0,.12);
  }

  /* Back side */
  .card-back {
    background: var(--navy);
    display: flex; flex-direction: column; align-items: center; justify-content: center;
    color: var(--paper);
  }
  .back-brand {
    font-family: "Marcellus", serif; font-size: 44px; letter-spacing: 2px;
    margin-top: -20px;
  }
  .back-url {
    position: absolute; bottom: 44px; left: 0; right: 0; text-align: center;
    font-family: "Cormorant Garamond", serif; font-weight: 500;
    font-size: 17px; letter-spacing: 3px; text-transform: uppercase;
  }

  /* Front side */
  .card-front { background: var(--paper); }
  .front-brand {
    position: absolute; top: 46px; left: 50px;
    font-family: "Marcellus", serif; font-size: 34px; letter-spacing: 1.5px;
    color: var(--navy);
  }
  .contact-list {
    position: absolute; top: 132px; left: 52px;
    list-style: none;
    font-family: "Cormorant Garamond", serif; font-weight: 600;
    font-size: 15px; color: var(--muted); line-height: 1.2;
  }
  .contact-list li { display: flex; align-items: center; gap: 10px; margin-bottom: 7px; }
  .contact-list .icon {
    flex: none; width: 16px; height: 16px; border-radius: 50%;
    background: var(--navy); display: flex; align-items: center; justify-content: center;
  }
  .contact-list .icon svg { width: 10px; height: 10px; fill: var(--paper); }
  .contact-list .indent { padding-left: 26px; margin-top: -5px; }

  .person {
    position: absolute; right: 60px; top: 258px; text-align: left;
    font-family: "Marcellus", serif; color: var(--navy);
  }
  .person-name { font-size: 20px; letter-spacing: 1.5px; text-transform: uppercase; }
  .person-role { font-family: "Cormorant Garamond", serif; font-weight: 600; font-size: 16px; color: var(--muted); letter-spacing: 1px; margin-top: 2px; }

  .front-band { position: absolute; left: 0; bottom: 0; width: 700px; height: 70px; }
  .front-url {
    position: absolute; right: 60px; bottom: 16px;
    font-family: "Cormorant Garamond", serif; font-weight: 600;
    font-size: 15px; letter-spacing: 3px; text-transform: uppercase; color: var(--paper);
  }
</style>
</head>
<body>
<main class="sheet">

  <section class="card card-back" aria-label="Business card, back">
    <p class="back-brand">Brightway Journeys</p>
    <p class="back-url">www.brightwayjourney.example</p>
  </section>

  <section class="card card-front" aria-label="Business card, front">
    <p class="front-brand">Brightway Journeys</p>

    <ul class="contact-list">
      <li><span class="icon"><svg viewBox="0 0 10 10"><path d="M5 0.5a3 3 0 0 0-3 3c0 2.3 3 6 3 6s3-3.7 3-6a3 3 0 0 0-3-3zm0 4.2a1.2 1.2 0 1 1 0-2.4 1.2 1.2 0 0 1 0 2.4z"/></svg></span>H. Fehimaage, Kanbaafaru Higun</li>
      <li class="indent">Male' Maldives.</li>
      <li><span class="icon"><svg viewBox="0 0 10 10"><path d="M2.2 1l1.6 1.9-.8 1.1a5.5 5.5 0 0 0 2.9 2.9l1.1-.8L9 7.8 8 9C4.5 9 1 5.5 1 2z"/></svg></span>+960 301 2468</li>
      <li><span class="icon"><svg viewBox="0 0 10 10"><rect x="2.5" y="0.8" width="5" height="8.4" rx="1"/></svg></span>+960 778 1234</li>
      <li><span class="icon"><svg viewBox="0 0 10 10"><rect x="1" y="3" width="8" height="5" rx="0.6"/><rect x="2.5" y="1" width="5" height="2.4"/></svg></span>+960 301 2469</li>
      <li><span class="icon"><svg viewBox="0 0 10 10"><path d="M1 2.5h8v5H1z"/><path d="M1 2.5l4 3 4-3" fill="none" stroke="#123a78" stroke-width="0.8"/></svg></span>naseer@brightwayjourney.example</li>
      <li><span class="icon"><svg viewBox="0 0 10 10"><circle cx="5" cy="5" r="3.6" fill="none" stroke="#fff" stroke-width="1"/><path d="M1.4 5h7.2M5 1.4c-1.6 2-1.6 5.2 0 7.2M5 1.4c1.6 2 1.6 5.2 0 7.2" fill="none" stroke="#fff" stroke-width="0.7"/></svg></span>www.brightwayjourney.example</li>
    </ul>

    <div class="person">
      <p class="person-name">Ibrahim Naseer</p>
      <p class="person-role">Managing Director</p>
    </div>

    <svg class="front-band" viewBox="0 0 700 70" preserveAspectRatio="none" aria-hidden="true">
      <rect x="0" y="38" width="700" height="32" fill="var(--orange)"/>
      <path d="M190 70 C220 70 220 22 260 22 L700 22 L700 70 Z" fill="var(--navy)"/>
    </svg>
    <p class="front-url">www.brightwayjourney.example</p>
  </section>

</main>
</body>
</html>
```